PSD web site UI

I need a PSD of a web site interface that I can use to build a theme with, which will be used on www.plovix.com, an up-and-coming CMS platform that I developed.

Follow the specifications included within the RAR file download below, and use the included PSD as a reference to make your own unique UI design.

Winners will be chosen based on how clean & professional the design looks, by how many unique panel designs are included within the UI, and by how large of a target market could actually use the design for their business web site.

Contest winners will only need to provide their PSD as completed work.

Download the PSD mockup at the bottom of this page to get started right away!
Updates

Project Deadline Extended
Reason: It was requested that I extend the deadline

Target Market(s)

small businesses and freelance designers, photographers & artists.

Industry/Entity Type

Business

Requirements
Must have
• Your PSD can have any color scheme you want. It can be light, dark, green, blue, multi-colored, paper, metallic, glossy, shiny, solid, gradients, or any theme you can imagine. Be creative, but keep the design looking Web 2.0 & professional. The width of your design can be 960 pixels wide like in the provided mockup PSD, or it can be a 100% width design if you'd like.

-
Panels
-
Each theme requires a minimum of 5 panel designs, which is basically a box that can stretch to a specific width or that stretches to 100% width of the web site. These 5 panels include a header, body, footer, child (that is placed within the body panel), and an alternative body panel. Of course, you can create as many panels as you like to create a more custom theme. Your panels do not have to look like the ones provided in the PSD mockup. They don't have to be completely square with round corners. They could be a bubbly cloud, or wavy, or include garnish around the edges, or be torn paper, or anything you like. Also, you can include a title within some of your panels, which is basically a header design with text at the top of the panel.

Each panel must contain a set of elements that fit the design of the panel. The body of your design should also include this set of elements. These elements include at least one menu, a set of buttons, lorum ipsum text & an anchor link, and form elements, such as a textbox, dropdown, & checkbox.

-
body
-
The body of your design should use a texture, gradient, solid color, or a background image that stretches 100% width. If you separate the body of your design into sectioned rows, each row will be treated like a panel.

-
Dashboard section
-
After a user logs into their account on Plovix.com, they manage their web site via a dashboard. This dashboard has a complex design, but can be partially customized. All elements within the header of the dashboard can be rearranged. This includes the title, screenshot, section title, and section menu. The main menu on the left contains a list of sections within the dashboard, which when clicked, will load the section title & menu in the dashboard header, and load the section page within the body of the dashboard.

Dashboard Icons:
The main menu & other menus within the dashboard contain icons. You can create your own custom icon library to use with your theme if you'd like, and the toolkit comes with a complete set of icons to use if you choose not to create your own library.

Dashboard body:
Each row within the dashboard body (options, search, results, paging) can use a panel design, but the entire dashboard body can also use a panel design as well, so you could design your dashboard body to use just one encompassing panel instead of separate panels for each row if you wanted.

-
Buttons
-
Each panel must contain a set of buttons. Each button requires a regular design as well as a mouse-over design. These types of buttons include: default, apply, cancel, previous, next, and delete (delete should stay small like a "close window" button).

-
Menus
-
Each menu requires a mouse-over design & selected item design.
You can make many types of menus; vertical, horizontal, small, and large.
Each item in the menu can be uniquely designed to create a sequence of menu items. For example, grey, white, grey, white, etc..

-
Photo Gallery
-
each photo container can be uniquely designed, creating a sequence of designs in a list.

-
Comments
-
each comment post can be uniquely designed, creating a sequence of designs in a list.
This will be used for comments as well as twitter feeds.

-
Blog Entries
-
Create designs for a blog summary list & a blog entry details.

Each blog entry (summary or details) can be uniquely designed, creating a sequence of designs in a list.

You could display a title, date created, tag words, summary, and the entry text, but you don't have to display all fields.

-
Product List
-
Products can be displayed many different ways:

product details, list grid, list rows, or even featured products list (with a flashy design).

You can display the product title, price, sale price & sale end date, description, photo & photo gallery, add to cart button, and view product details button. You don't have to display all fields for each design. You could show just a photo & title with summary & no price, or just a photo & title, or just the photo if you wanted.

-
Form elements
-
The textbox can look completely custom, have rounded corners, a textured background, or look plain if you want. The other form elements on the other hand can only be manipulated by CSS, so are very limited in design. Only border color, background color, and text color can be changed. The drop down box can have a custom drop down arrow though.

-
Header Panel
-
Requires a horizontal menu system that can be used for the web site's main menu

-
Footer Panel
-
The footer should be 100% width. Many web sites these days have very creative footers.
Should not have
• Don't use the mockup to just make color changes. I want a completely custom design that uses the structure of the mockup, but has a unique theme to the design, such as paper, dark grungy, cartoonish, hand-drawn, etc. Impress me & impress yourself!

```html
<!DOCTYPE html>
<html lang="en">
<head>
<meta charset="utf-8">
<title>Plovix Theme UI</title>
<link rel="stylesheet" href="https://fonts.googleapis.com/css2?family=Open+Sans:wght@300;400;600;700&family=Arimo:wght@400;700&display=swap">
<style>
:root{
  --blue:#2b5294;--blue-dark:#1f3f78;--page:#ffffff;--panel:#f7f7f7;--line:#cfcfcf;
  --ink:#333;--ink-soft:#666;--mute:#999;--dark:#4a4a4a;--darker:#3a3a3a;
  --btn-top:#f2f2f2;--btn-bot:#d9d9d9;--gbtn-top:#8a8a8a;--gbtn-bot:#5f5f5f;
  --link:#2a64b6;--price:#1ea0e6;--red:#e2452b;
}
*{box-sizing:border-box;margin:0;padding:0}
html,body{width:1200px;height:2326px;overflow:hidden}
body{position:relative;background:var(--page);font-family:"Open Sans",sans-serif;color:var(--ink)}
.abs{position:absolute}
.panel{position:absolute;background:var(--panel);border:1px solid var(--line);border-radius:7px;box-shadow:0 1px 2px rgba(0,0,0,.08)}
.btn{position:absolute;display:flex;align-items:center;justify-content:center;gap:8px;border:1px solid #bdbdbd;border-radius:4px;background:linear-gradient(var(--btn-top),var(--btn-bot));font-size:15px;color:#555}
.gbtn{position:absolute;display:flex;align-items:center;justify-content:center;border-radius:3px;background:linear-gradient(var(--gbtn-top),var(--gbtn-bot));color:#fff;font-size:12px;font-weight:600;border:1px solid #555}
.arrow-l{clip-path:polygon(12px 0,100% 0,100% 100%,12px 100%,0 50%)}
.arrow-r{clip-path:polygon(0 0,calc(100% - 12px) 0,100% 50%,calc(100% - 12px) 100%,0 100%)}
.field{position:absolute;background:#fff;border:1px solid #c9c9c9;border-radius:7px;font-size:14px;color:#999;padding-left:16px;display:flex;align-items:center}
.ico{display:inline-block;width:16px;height:16px}
/* header */
.site-header{position:absolute;left:0;top:0;width:1200px;height:120px;background:linear-gradient(#34609f,var(--blue-dark))}
.brand{position:absolute;font-weight:400;letter-spacing:1px;color:#e8edf5}
.main-nav a{position:absolute;color:#dfe7f3;font-size:18px;text-decoration:none}
.main-nav .current{background:#1b1b1b;border:1px solid #555;border-radius:3px;color:#fff;display:flex;align-items:center;justify-content:center}
/* sidebar */
.side-menu li{position:absolute;left:6px;width:157px;height:31px;list-style:none;display:flex;align-items:center;gap:10px;padding-left:12px;font-size:16px;color:#444}
.side-menu li.hover{background:linear-gradient(#fbfbfb,#e9e9e9);border:1px solid #d6d6d6;border-radius:3px}
.side-menu li.selected{background:linear-gradient(#e6e6e6,#cfcfcf);border:1px solid #bdbdbd;border-radius:3px}
.entry h3{font-weight:400;font-size:19px;color:#222}
.entry p,.lorem{font-family:Arimo,sans-serif;font-size:11.6px;line-height:19.5px;color:#444}
.del{position:absolute;width:14px;height:14px}
/* dark menu */
.dmenu li{position:absolute;list-style:none;width:117px;height:31px;display:flex;align-items:center;gap:8px;padding-left:10px;font-size:16px;color:#eee}
.dmenu li.sel{background:linear-gradient(#8a8a8a,#6b6b6b);border:1px solid #aaa;border-radius:3px}
.dmenu li.hov{background:linear-gradient(#6c6c6c,#555);border:1px solid #888;border-radius:3px}
.wbtn{position:absolute;background:linear-gradient(#fff,#e4e4e4);border:1px solid #bbb;border-radius:3px;font-size:12px;color:#333;display:flex;align-items:center;padding-left:14px}
.dlink{position:absolute;color:#e8e8e8;text-decoration:underline;font-size:16px}
.photo{position:absolute;border:1px solid #ddd;padding:3px;background:#fff}
.photo div{width:100%;height:100%}
/* comments */
.comment .avatar{position:absolute;left:18px;top:22px;width:48px;height:48px;background:#e2e2e2;border:1px solid #ccc}
.comment .user{position:absolute;left:17px;top:76px;font-size:11.5px;color:var(--link)}
.comment p{position:absolute;left:95px;top:16px;width:510px;font-family:Arimo,sans-serif;font-size:11px;line-height:20px;color:#444}
.comment .when{position:absolute;left:95px;top:74px;font-size:11px;color:#777;border-top:1px solid #ddd;width:515px;padding-top:9px}
/* calendar */
.cal{position:absolute;left:787px;top:1052px;width:290px;height:253px;background:#e9e9e9}
.cal-title{height:47px;background:linear-gradient(#6a6a6a,#464646);color:#fff;font-weight:700;font-size:24px;display:flex;align-items:center;justify-content:center;font-family:Arimo,sans-serif}
.cal-days{display:grid;grid-template-columns:repeat(7,1fr);height:15px;font-size:10px;font-weight:700;text-align:center;line-height:15px}
.cal-grid{display:grid;grid-template-columns:repeat(7,1fr);grid-auto-rows:41px;font-family:Arimo,sans-serif;font-weight:700;font-size:14px;color:#333}
.cal-grid span{display:flex;align-items:center;justify-content:center;border-bottom:1px solid #dcdcdc}
.cal-grid .out{color:#aaa}.cal-grid .today{color:var(--link)}
/* blog */
.card{position:absolute;background:#fff;border-radius:4px}
.card h4{font-weight:400;font-size:16.5px;line-height:19px;color:#333}
.card p{font-size:11.5px;line-height:18px;color:#888}
.footer{position:absolute;left:0;top:2155px;width:1200px;height:171px;background:var(--dark)}
</style>
</head>
<body>

<header class="site-header">
  <div class="brand" style="left:110px;top:34px;font-size:42px">PLOVIX</div>
  <nav class="main-nav">
    <a class="current" style="left:651px;top:39px;width:112px;height:42px">Dashboard</a>
    <a style="left:783px;top:48px">Community</a>
    <a style="left:906px;top:48px">Developers</a>
    <a style="left:1022px;top:48px">Support</a>
  </nav>
</header>

<!-- dashboard header -->
<section class="panel" style="left:110px;top:140px;width:980px;height:128px">
  <div role="img" aria-label="Website screenshot thumbnail with desert landscape" class="abs" style="left:14px;top:8px;width:150px;height:110px;border-radius:4px;background:linear-gradient(#8c6a52,#c89a74 45%,#4e3a30)"></div>
  <div class="abs" style="left:192px;top:-2px;font-size:33px;font-weight:300;color:#444">Dana Whitfield</div>
  <svg class="abs" style="left:192px;top:96px" width="50" height="20" viewBox="0 0 50 20"><path d="M2 8v10h16v-6" fill="none" stroke="#555" stroke-width="2"/><path d="M7 13c2-6 6-8 12-8V1l6 6-6 6V9c-5 0-8 1-12 4z" fill="#555"/><rect x="32" y="4" width="13" height="14" fill="none" stroke="#555" stroke-width="2"/><path d="M38 13l9-10 2 2-9 10-3 1z" fill="#555"/></svg>
  <div class="btn" style="left:796px;top:12px;width:169px;height:56px;font-size:21px;border-radius:6px"><span style="width:26px;height:30px;background:#3d7a2c;border-radius:3px"></span>Blog Book</div>
  <div class="btn" style="left:796px;top:79px;width:169px;height:35px;font-size:14px"><svg class="ico" viewBox="0 0 16 16"><rect x="2" y="1" width="12" height="14" fill="none" stroke="#555"/></svg>Create New Entry</div>
</section>

<!-- sidebar menu -->
<nav class="panel" style="left:113px;top:276px;width:169px;height:291px">
  <ul class="side-menu">
    <li style="top:8px"><svg class="ico" viewBox="0 0 16 16"><rect x="3" y="1" width="10" height="14" fill="#fff" stroke="#666"/></svg>Pages</li>
    <li style="top:43px"><svg class="ico" viewBox="0 0 16 16"><rect x="1" y="2" width="14" height="12" fill="#7aa6c9" stroke="#555"/></svg>Media</li>
    <li style="top:78px"><svg class="ico" viewBox="0 0 16 16"><path d="M1 2h14v9H6l-3 3v-3H1z" fill="#fff" stroke="#555"/></svg>Messages</li>
    <li class="hover" style="top:113px"><svg class="ico" viewBox="0 0 16 16"><rect x="1" y="1" width="14" height="14" fill="#fff" stroke="#555"/><path d="M3 12l3-4 3 2 4-6" stroke="#555" fill="none"/></svg>Analytics</li>
    <li style="top:148px"><svg class="ico" viewBox="0 0 16 16"><rect x="2" y="1" width="12" height="14" fill="#fff" stroke="#555"/></svg>Site Map</li>
    <li style="top:183px"><svg class="ico" viewBox="0 0 16 16"><rect x="2" y="2" width="12" height="12" fill="#fff" stroke="#555"/></svg>Settings</li>
    <li style="top:218px"><svg class="ico" viewBox="0 0 16 16"><path d="M8 1l7 4v6l-7 4-7-4V5z" fill="#fff" stroke="#555"/></svg>Install Apps</li>
    <li class="selected" style="top:253px"><span class="ico" style="background:#3d7a2c;border-radius:2px"></span>Blog Book</li>
  </ul>
</nav>

<!-- options -->
<section class="panel" style="left:287px;top:276px;width:803px;height:130px">
  <div class="abs" style="left:14px;top:20px;font-size:15px">Select Folder :</div>
  <div class="field" style="left:125px;top:13px;width:276px;height:36px"><svg class="abs" style="right:12px;top:13px" width="12" height="8"><path d="M1 1l5 5 5-5" fill="none" stroke="#666" stroke-width="2"/></svg></div>
  <div class="btn" style="left:14px;top:76px;width:172px;height:36px;font-size:14px"><span class="ico" style="border:1px solid #666;width:13px;height:14px"></span>Create New Entry</div>
  <div class="btn" style="left:193px;top:76px;width:168px;height:36px;font-size:14px"><span class="ico" style="background:#666;width:12px;height:13px"></span>Select All Enteries</div>
  <div class="btn" style="left:369px;top:76px;width:269px;height:36px;font-size:14px"><span class="ico" style="background:#666;width:18px;height:12px"></span>Move Selected Entries to Folder</div>
</section>

<!-- search -->
<section class="panel" style="left:287px;top:411px;width:803px;height:49px">
  <div class="field" style="left:14px;top:7px;width:304px;height:34px;border-radius:7px 0 0 7px;font-size:13px;color:#555">Search blog entries</div>
  <div class="btn" style="left:317px;top:7px;width:84px;height:34px;border-radius:0 7px 7px 0">Search</div>
</section>

<!-- results -->
<article class="panel entry" style="left:287px;top:467px;width:803px;height:110px">
  <span class="abs" style="left:32px;top:17px;width:13px;height:13px;border:1px solid #999;background:#eee"></span>
  <h3 class="abs" style="left:62px;top:7px">A day in the life of Leo Marsh.</h3>
  <p class="abs" style="left:62px;top:37px;width:705px">Morbi id lacus eget nulla feugiat tempus in et felis. Quisque accumsan tortor eu orci varius ultricies. Vestibulum ante ipsum primis in faucibus orci luctus et ultrices posuere cubilia Curae; Aenean cursus, nisl vitae vehicula vulputate, erat tellus porttitor odio, vitae suscipit mauris.</p>
  <svg class="del" style="left:770px;top:15px" viewBox="0 0 14 14"><path d="M2 2l10 10M12 2L2 12" stroke="var(--red)" stroke-width="3"/></svg>
</article>
<article class="panel entry" style="left:287px;top:584px;width:803px;height:110px">
  <span class="abs" style="left:32px;top:17px;width:13px;height:13px;border:1px solid #999;background:#eee"></span>
  <h3 class="abs" style="left:62px;top:7px">A day in the life of Leo Marsh.</h3>
  <p class="abs" style="left:62px;top:37px;width:705px">Morbi id lacus eget nulla feugiat tempus in et felis. Quisque accumsan tortor eu orci varius ultricies. Vestibulum ante ipsum primis in faucibus orci luctus et ultrices posuere cubilia Curae; Aenean cursus, nisl vitae vehicula vulputate, erat tellus porttitor odio, vitae suscipit mauris.</p>
  <svg class="del" style="left:770px;top:15px" viewBox="0 0 14 14"><path d="M2 2l10 10M12 2L2 12" stroke="var(--red)" stroke-width="3"/></svg>
</article>

<!-- paging -->
<div class="gbtn arrow-l" style="left:908px;top:705px;width:103px;height:27px">Previous</div>
<div class="gbtn arrow-r" style="left:1017px;top:705px;width:73px;height:27px">More</div>

<!-- dark alternative panel -->
<section class="abs" style="left:110px;top:753px;width:980px;height:132px;border-radius:6px;background:linear-gradient(#6a6a6a,#4d4d4d 50%,#444)">
  <ul class="dmenu">
    <li class="sel" style="left:10px;top:13px"><span class="ico" style="background:#dde;width:13px"></span>Pages</li>
    <li class="hov" style="left:10px;top:48px"><span class="ico" style="background:#9bc"></span>Media</li>
    <li style="left:10px;top:83px"><span class="ico" style="background:#eee;height:12px"></span>Messages</li>
  </ul>
  <div class="wbtn" style="left:209px;top:12px;width:115px;height:30px">Browse<svg class="abs" style="right:12px;top:8px" width="14" height="14"><path d="M2 2l10 10M12 2L2 12" stroke="var(--red)" stroke-width="3"/></svg></div>
  <div class="wbtn" style="left:209px;top:52px;width:115px;height:30px">Apply</div>
  <div class="abs" style="left:209px;top:92px;font-size:16px;color:#eee">Lorem ipsum dolor sit amet</div>
  <a class="dlink" style="left:420px;top:92px">Click here</a>
  <div class="abs" style="left:530px;top:0;width:2px;height:132px;background:#333"></div>
  <div class="abs" style="left:552px;top:47px;width:98px;height:39px;background:#1f1f1f;border:1px solid #666;border-radius:3px;color:#fff;font-size:18px;display:flex;align-items:center;justify-content:center">Projects</div>
  <div class="abs" style="left:688px;top:55px;font-size:18px;color:#ddd">Team</div>
  <div class="abs" style="left:787px;top:55px;font-size:18px;color:#ddd">Mantra</div>
  <div class="abs" style="left:892px;top:55px;font-size:18px;color:#ddd">Contact</div>
</section>

<!-- gallery -->
<div class="photo" style="left:110px;top:900px;width:210px;height:128px"><div role="img" aria-label="Photo of a white cruise ship near a green island" style="background:linear-gradient(#8fc2ea,#2d6fb4 45%,#1e4f9a)"></div></div>
<div class="photo" style="left:331px;top:900px;width:212px;height:128px"><div role="img" aria-label="Illustration of a tree by a pond in a meadow" style="background:linear-gradient(#e9f1d6,#b8d67a 55%,#7aa943)"></div></div>
<div class="photo" style="left:551px;top:900px;width:211px;height:128px"><div role="img" aria-label="Photo of sunlit forest with tall pine trees" style="background:linear-gradient(#d6e6b8,#7b9a4a 55%,#3d5a25)"></div></div>
<section class="abs" style="left:773px;top:900px;width:317px;height:128px;border:1px solid #ddd;padding:3px;background:#fff">
  <div class="abs" style="left:3px;top:3px;right:3px;bottom:3px;background:#4a4a4a"></div>
  <ul class="dmenu">
    <li class="sel" style="left:28px;top:16px;width:115px"><span class="ico" style="background:#dde;width:13px"></span>Pages</li>
    <li class="hov" style="left:28px;top:51px;width:115px"><span class="ico" style="background:#9bc"></span>Media</li>
    <li style="left:28px;top:86px"><span class="ico" style="background:#eee;height:12px"></span>Messages</li>
  </ul>
  <div class="wbtn" style="left:175px;top:14px;width:115px;height:30px">Browse<svg class="abs" style="right:12px;top:8px" width="14" height="14"><path d="M2 2l10 10M12 2L2 12" stroke="var(--red)" stroke-width="3"/></svg></div>
  <div class="wbtn" style="left:175px;top:54px;width:115px;height:30px">Apply</div>
  <a class="dlink" style="left:180px;top:95px">Click here</a>
</section>

<!-- comments -->
<article class="panel comment" style="left:110px;top:1052px;width:650px;height:111px">
  <div class="avatar"></div><div class="user">Username</div>
  <p>Morbi id lacus eget nulla feugiat tempus in et felis. Quisque accumsan tortor eu orci varius ultricies.</p>
  <div class="when">about 20 mints ago</div>
</article>
<article class="panel comment" style="left:110px;top:1173px;width:650px;height:111px">
  <div class="avatar"></div><div class="user">Username</div>
  <p>Morbi id lacus eget nulla feugiat tempus in et felis. Quisque accumsan tortor eu orci varius ultricies.</p>
  <div class="when">about 20 mints ago</div>
</article>
<div class="gbtn" style="left:110px;top:1299px;width:144px;height:28px">Leave a Comment</div>
<div class="gbtn arrow-r" style="left:685px;top:1299px;width:75px;height:28px">More</div>

<!-- calendar -->
<section class="cal">
  <div class="cal-title">February 2013</div>
  <div class="cal-days">
    <span style="background:#2f8fd8;color:#123">SUN</span><span style="background:#3cb0c4">MON</span><span style="background:#b9c73a">TUE</span><span style="background:#e8a12a">WED</span><span style="background:#ec7b2a">THU</span><span style="background:#e23a3a">FRI</span><span style="background:#a04bc9">SAT</span>
  </div>
  <div class="cal-grid">
    <span>1</span><span>2</span><span class="today">3</span><span>4</span><span>5</span><span>6</span><span>7</span>
    <span>8</span><span>9</span><span>10</span><span>11</span><span>12</span><span>13</span><span>14</span>
    <span>15</span><span>16</span><span>17</span><span>18</span><span>19</span><span>20</span><span>21</span>
    <span>22</span><span>23</span><span>24</span><span>25</span><span>26</span><span>27</span><span>28</span>
    <span>29</span><span>30</span><span>31</span><span class="out">1</span><span class="out">2</span><span class="out">3</span><span class="out">4</span>
  </div>
</section>

<!-- comment form -->
<section class="panel" style="left:110px;top:1353px;width:650px;height:341px">
  <div class="abs" style="left:14px;top:21px;font-size:16px;color:#444">Leave a comment</div>
  <div class="field" style="left:14px;top:57px;width:276px;height:35px">your name</div>
  <div class="field" style="left:324px;top:57px;width:276px;height:35px">Web site (optional)</div>
  <div class="field" style="left:14px;top:109px;width:276px;height:35px">your email</div>
  <div class="field" style="left:14px;top:158px;width:586px;height:112px"></div>
  <div class="gbtn" style="left:457px;top:293px;width:143px;height:28px">Submit Comment</div>
</section>

<!-- blog & products -->
<section class="panel" style="left:110px;top:1714px;width:980px;height:402px">
  <h2 class="abs" style="left:34px;top:22px;font-weight:400;font-size:31px;color:#444">Build a startup, not a resume.</h2>
  <div class="abs" style="left:36px;top:67px;font-size:13px;color:#999">Published Friday, September 13th.</div>
  <p class="abs lorem" style="left:36px;top:96px;width:614px;line-height:19px">Mauris ultricies urna id mauris convallis eu placerat purus ornare. Pellentesque in quam vel mauris placerat fermentum. Nullam imperdiet auctor arcu eu tincidunt. Nullam faucibus, orci in sodales tincidunt, eros justo rhoncus arcu, a consectetur dui ipsum nec nulla. Nam congue arcu massa. Sed accumsan risus sit amet dolor tincidunt in molestie mi hendrerit. Etiam semper pulvinar eros sollicitudin fermentum. Suspendisse potenti. Nunc sit amet leo non erat volutpat tempor at eget purus. Vestibulum ante ipsum primis in faucibu.</p>
  <div class="card" style="left:40px;top:220px;width:279px;height:171px">
    <h4 class="abs" style="left:11px;top:13px">Spending money<br>the right way.</h4>
    <p class="abs" style="left:11px;top:60px;width:260px">Why is it that we buy things that we don't need at all? I'll share my secrets with you on how to make money by spending money!</p>
    <div class="gbtn" style="left:149px;top:124px;width:124px;height:28px">Read more</div>
  </div>
  <div class="card" style="left:350px;top:220px;width:281px;height:171px">
    <h4 class="abs" style="left:11px;top:13px">Spending money<br>the right way.</h4>
    <p class="abs" style="left:11px;top:60px;width:260px">Why is it that we buy things that we don't need at all? I'll share my secrets with you on how to make money by spending money!</p>
    <div class="gbtn" style="left:151px;top:124px;width:124px;height:28px">Read more</div>
  </div>
  <div class="card" style="left:670px;top:14px;width:296px;height:377px">
    <div role="img" aria-label="Photo of a city park with skyline" class="abs" style="left:15px;top:25px;width:149px;height:157px;border:1px solid #ddd;background:linear-gradient(#9fc7ee,#cdd9e6 40%,#5d8b3a 65%,#3f6b27)"></div>
    <div class="abs" style="left:180px;top:25px;font-size:23px;color:#444">Slate mini</div>
    <div class="abs" style="left:180px;top:58px;color:var(--price);font-size:15px">now <span style="font-size:27px">$429</span></div>
    <div class="gbtn" style="left:180px;top:105px;width:102px;height:28px">Buy Now</div>
    <p class="abs" style="left:15px;top:207px;width:270px;font-size:11.5px;line-height:18px;color:#888">Why is it that we buy things that we don't need at all? I'll share my secrets with you on how to make money by spending money!</p>
    <div role="img" aria-label="Product photo of a white tablet held in a hand" class="abs" style="left:15px;top:268px;width:88px;height:95px;border:1px solid #ddd;background:linear-gradient(#f1f1f1,#cfd6dd)"></div>
    <div class="abs" style="left:122px;top:274px;font-size:19px;color:#444">Slate Mini</div>
    <div class="abs" style="left:122px;top:302px;font-size:13px;color:var(--price)">$429 <sup style="font-size:8px">00</sup></div>
  </div>
</section>

<!-- footer -->
<footer class="footer">
  <div class="brand" style="left:110px;top:14px;font-size:42px;color:#ddd">PLOVIX</div>
  <a class="dlink" style="left:110px;top:72px;color:#cfd8e8">Click here</a>
  <ul class="dmenu">
    <li class="sel" style="left:340px;top:18px"><span class="ico" style="background:#dde;width:13px"></span>Pages</li>
    <li class="hov" style="left:340px;top:53px"><span class="ico" style="background:#9bc"></span>Media</li>
    <li style="left:340px;top:88px"><span class="ico" style="background:#eee;height:12px"></span>Messages</li>
  </ul>
  <div class="wbtn" style="left:489px;top:16px;width:115px;height:30px">Browse<svg class="abs" style="right:12px;top:8px" width="14" height="14"><path d="M2 2l10 10M12 2L2 12" stroke="var(--red)" stroke-width="3"/></svg></div>
  <div class="wbtn" style="left:489px;top:56px;width:115px;height:30px">Apply</div>
</footer>

</body>
</html>
```